Small Ecommerce Styled Site to Sell / Lease Domain Names

We have a small portfolio of 100+ domain names that we would like to offer for sale or lease via a web site. Along the lines of http://www.velramarkets.com/searchdomain.html?priceChoice=2&sort=leasing_desc

We would like initially a 4 page design, listing page (as site referenced above), domain info page (Universal Domain Name Landing Page with form) and checkout a page and About Us Page

We do not want a replica of the site listed, please use it as a guide only, we are looking for a fresh design, in similar concept web 2.0

Our Colours are #351a41 (Main) - #ffca27 (Secondary) all other colours must compliment those 2.
Updates

Domain Landing Page:  I am sorry I was not clear about expectations, however we would like a domain landing page that would be the default holding page for a domain name.

For some examples of what I mean please see:
https://www.pobexhub.com.au/guest-articles/7626-domain-for-sale-landing-pages.html
http://dev.quillterbrokers.com/blog/2013/09/sales-only-landers-and-buy-it-now-2/

Industry/Entity Type

Domain

Font styles to use
Sans Serif

```html
<!DOCTYPE html>
<html lang="en">
<head>
<meta charset="utf-8">
<title>Leasewell — Affordable Domain Solution</title>
<link href="https://fonts.googleapis.com/css2?family=Open+Sans:wght@300;400;600&family=PT+Sans:wght@400;700&display=swap" rel="stylesheet">
<style>
:root{
  --plum:#351a41;
  --gold:#ffca27;
  --ink:#222;
  --muted:#7a7a7a;
  --line:#e3e3e3;
  --footer:#2b2b2b;
  --footer-base:#1c1c1c;
  --white:#fff;
}
*{box-sizing:border-box;margin:0;padding:0}
html,body{width:743px;height:1200px;overflow:hidden}
body{position:relative;background:var(--white);font-family:"Open Sans",sans-serif;color:var(--ink)}
.abs{position:absolute}
ul{list-style:none}

/* header */
.brand{left:73px;top:10px;font-family:"PT Sans",sans-serif;font-size:25px;letter-spacing:.5px;color:var(--ink)}
.account{top:17px;left:398px;display:flex;gap:0;font-size:9.5px;color:#555;align-items:center}
.account span{display:flex;align-items:center;gap:4px;margin-right:17px}
.account svg{width:11px;height:11px}
.flag{width:10px;height:7px;background:#b22234;display:inline-block;position:relative}
.flag::before{content:"";position:absolute;left:0;top:0;width:4px;height:4px;background:#3c3b6e}
.nav{left:0;top:48px;width:743px;height:32px;background:var(--gold)}
.nav ul{position:absolute;left:74px;top:0;display:flex;height:32px;border-left:1px solid rgba(0,0,0,.12)}
.nav li{height:32px;display:flex;align-items:center;justify-content:center;color:var(--white);font-size:10px;border-right:1px solid rgba(0,0,0,.12)}

/* hero */
.hero{left:0;top:80px;width:743px;height:323px;background:linear-gradient(100deg,#8f8f8f 0%,#a4a4a4 45%,#8a8580 70%,#7b6a55 100%)}
.hero-title{left:0;top:151px;width:706px;text-align:center;font-size:24px;color:var(--gold);font-weight:400}
.hero-text{left:130px;top:192px;width:446px;text-align:center;font-size:9px;line-height:15px;color:var(--white)}
.search-input{left:128px;top:252px;width:358px;height:42px;background:var(--white);font-size:13px;color:#888;padding:0 12px;display:flex;align-items:center}
.search-btn{left:492px;top:252px;width:116px;height:42px;background:var(--plum);color:var(--white);font-size:17px;display:flex;align-items:center;justify-content:center;letter-spacing:.5px}

/* sidebar */
.panel{border:1px solid var(--line);border-left:4px solid var(--gold);background:var(--white)}
.categories{left:74px;top:434px;width:181px;height:397px}
.panel-title{height:36px;display:flex;align-items:center;padding-left:14px;font-size:16px;color:#555;border-bottom:1px solid var(--line)}
.categories .panel-title{font-size:16.5px;letter-spacing:.3px}
.categories li{height:30px;display:flex;align-items:center;padding-left:12px;font-size:11.5px;color:#666;border-bottom:1px solid var(--line)}
.categories li:last-child{border-bottom:0}
.structure{left:74px;top:849px;width:181px;height:163px}
.structure .panel-title{height:34px;padding-left:11px;font-size:14.5px}
.field{display:flex;align-items:center;justify-content:space-between;padding:0 11px 0 15px;height:29px;font-size:8px;color:#888}
.field:first-of-type{margin-top:5px}
.field i{width:96px;height:16px;border:1px solid #ddd;background:#f9f9f9;display:block}
.checks{display:flex;gap:16px;padding:10px 0 0 15px;font-size:7px;color:#888}
.checks span{display:flex;align-items:center;gap:6px}
.checks b{width:7px;height:7px;border:1px solid #999;border-radius:50%;display:block}

/* listings */
.listings{left:272px;top:434px;width:395px;height:578px;border:1px solid var(--line)}
.steps{left:0;top:26px;width:395px;height:50px}
.steps .track{position:absolute;left:80px;top:14px;width:202px;height:3px;background:#eee}
.step{position:absolute;top:0;width:60px;text-align:center;font-size:9.5px;color:#777}
.step b{display:block;margin:0 auto 6px;width:27px;height:27px;border-radius:50%;background:#eee;border:2px solid #f5f5f5;color:#999;font-size:14px;font-weight:400;line-height:23px;position:relative}
.step.active b{background:var(--plum);color:var(--white);border-color:#ddd}
.listing{left:0;width:393px;border-top:1px solid var(--line)}
.listing.first{border-top:0}
.listing h3{position:absolute;left:16px;top:20px;font-weight:400;font-size:15px;color:#555}
.row{position:absolute;left:16px;top:46px;width:362px;height:24px;display:flex;align-items:center}
.rent{font-size:15px;font-weight:600;color:#666;width:31px}
.off{font-size:9.5px;color:#999;width:65px}
.cat-label{font-size:10px;color:#999;width:48px}
.select{width:47px;height:18px;border:1px solid #ddd;display:flex;font-size:8px;color:#888}
.select span{flex:1;display:flex;align-items:center;justify-content:center;border-right:1px solid #ddd}
.select em{width:17px;display:flex;align-items:center;justify-content:center;font-style:normal;font-size:6px;line-height:5px;color:#bbb;flex-direction:column}
.total{margin-left:21px;font-size:15px;font-weight:600;color:#666}
.offer{position:absolute;right:0;top:0;width:88px;height:24px;background:var(--plum);color:var(--white);font-size:12.5px;display:flex;align-items:center;justify-content:center}
.listing p{position:absolute;left:16px;top:85px;font-size:7.5px;color:#888}

/* footer */
.footer{left:0;top:1043px;width:743px;height:132px;background:var(--footer)}
.footer h4{position:absolute;top:24px;font-weight:400;font-size:11.5px;color:var(--white)}
.footer .col{position:absolute;top:54px}
.footer .about{left:74px;width:125px;font-size:7.2px;line-height:11px;color:#bbb}
.footer ul li{font-size:7.5px;line-height:11.2px;color:#bbb;padding-left:10px;position:relative}
.footer ul li::before{content:"";position:absolute;left:1px;top:5px;width:2px;height:2px;background:#bbb;border-radius:50%}
.newsletter-text{left:534px;width:138px;font-size:7.2px;line-height:12px;color:#bbb}
.newsletter-input{left:534px;top:94px;width:134px;height:21px;background:var(--white);font-size:7px;color:#999;display:flex;align-items:center;padding-left:5px}
.newsletter-input svg{position:absolute;right:7px;top:7px}
.base{left:0;top:1175px;width:743px;height:25px;background:var(--footer-base);color:#ddd;font-size:7.5px;display:flex;align-items:center;justify-content:center;padding-left:20px}
</style>
</head>
<body>

<header>
  <div class="abs brand">LEASEWELL</div>
  <div class="abs account">
    <span>Sing in <svg viewBox="0 0 12 12" fill="none" stroke="#666" stroke-width="1.2"><path d="M6 1v7M3 5l3 3 3-3M1 8v3h10V8"/></svg></span>
    <span>Sing out <svg viewBox="0 0 12 12" fill="none" stroke="#666" stroke-width="1.2"><path d="M6 9V1M3 4l3-3 3 3M1 8v3h10V8"/></svg></span>
    <span>Cart <svg viewBox="0 0 12 12" fill="#666"><path d="M0 1h2l2 6h6l1.5-4.5H3.2" fill="none" stroke="#666" stroke-width="1.1"/><circle cx="5" cy="10" r="1"/><circle cx="9" cy="10" r="1"/></svg></span>
    <span>Faq <svg viewBox="0 0 12 12" fill="none" stroke="#777" stroke-width="1"><circle cx="6" cy="6" r="5.3"/><path d="M4.5 4.6a1.5 1.5 0 1 1 1.5 1.6v1"/><circle cx="6" cy="8.9" r=".4" fill="#777"/></svg></span>
    <span><i class="flag"></i>▾ USA ▾</span>
  </div>
  <nav class="abs nav">
    <ul>
      <li style="width:50px">Home</li>
      <li style="width:76px">Buy Domins</li>
      <li style="width:86px">Lease Domins</li>
      <li style="width:70px">Categories</li>
      <li style="width:60px">Valution</li>
      <li style="width:58px">Affiliate</li>
      <li style="width:68px;border-right:0">Contact Us</li>
    </ul>
  </nav>
</header>

<section class="abs hero" role="img" aria-label="Photo of a woman in an orange top working on a laptop"></section>
<h1 class="abs hero-title">AFFORDABLE DOMAIN SOLUTION</h1>
<p class="abs hero-text">Sed ut perspiciatis unde omnis iste natus error sit voluptatem accusantium doloremque laudantium, totam rem aperiam, eaque ipsa quae ab illo inventore veritatis et quasi architecto beatae.</p>
<div class="abs search-input">Enter Key For Domain</div>
<div class="abs search-btn">SEARCH</div>

<aside class="abs panel categories">
  <div class="panel-title">CATEGORIES</div>
  <ul>
    <li>Automotive</li><li>Business and Finance</li><li>Computers and</li><li>Internet</li>
    <li>Education</li><li>Entertainment</li><li>Family</li><li>Food and Beverage</li>
    <li>Games</li><li>Home and Garden</li><li>Health and Beauty</li><li>Lifestyle</li>
  </ul>
</aside>

<aside class="abs panel structure">
  <div class="panel-title">Word Structure</div>
  <div class="field">Beung s With: <i></i></div>
  <div class="field">Ends With: <i></i></div>
  <div class="field">Exclude: <i></i></div>
  <div class="checks"><span><b></b>Disallow Hyphen</span><span><b></b>Disallow Number</span></div>
</aside>

<main class="abs listings">
  <div class="abs steps">
    <div class="track"></div>
    <div class="step active" style="left:50px"><b>1</b>Domain</div>
    <div class="step" style="left:118px"><b>2</b>Category</div>
    <div class="step" style="left:184px"><b>3</b>Leaes Fee</div>
    <div class="step" style="left:251px"><b>4</b>Price</div>
  </div>

  <article class="abs listing first" style="top:74px;height:122px">
    <h3>Lease Domain.com</h3>
    <div class="row"><span class="rent">$50</span><span class="off">30% Off</span><span class="cat-label">Category</span><span class="select"><span>05</span><em>▲<br>▼</em></span><span class="total">$250</span><span class="offer">Make Offer</span></div>
    <p>Lorem Ipsum is simply 's standard dummy text ever since the 1500s.</p>
  </article>
  <article class="abs listing" style="top:196px;height:118px">
    <h3>Lease Domain.com</h3>
    <div class="row"><span class="rent">$98</span><span class="off">30% Off</span><span class="cat-label">Category</span><span class="select"><span>05</span><em>▲<br>▼</em></span><span class="total">$450</span><span class="offer">Make Offer</span></div>
    <p>Lorem Ipsum is simply 's standard dummy text ever since the 1500s.</p>
  </article>
  <article class="abs listing" style="top:314px;height:123px">
    <h3>Lease Domain.com</h3>
    <div class="row"><span class="rent">$98</span><span class="off">30% Off</span><span class="cat-label">Category</span><span class="select"><span>05</span><em>▲<br>▼</em></span><span class="total">$450</span><span class="offer">Make Offer</span></div>
    <p>Lorem Ipsum is simply 's standard dummy text ever since the 1500s.</p>
  </article>
  <article class="abs listing" style="top:437px;height:140px">
    <h3>Lease Domain.com</h3>
    <div class="row"><span class="rent">$98</span><span class="off">30% Off</span><span class="cat-label">Category</span><span class="select"><span>05</span><em>▲<br>▼</em></span><span class="total">$450</span><span class="offer">Make Offer</span></div>
    <p>Lorem Ipsum is simply 's standard dummy text ever since the 1500s.</p>
  </article>
</main>

<footer class="abs footer">
  <h4 style="left:74px">Conatct Us</h4>
  <p class="col about">On the other hand, we denounce with righteous indignation and dislike men who are so beguiled and demoralized by the charms.</p>
  <h4 style="left:223px">Our Services</h4>
  <ul class="col" style="left:223px"><li>Lorem ipsum</li><li>Lorem ipsum</li><li>Lorem ipsum</li><li>Lorem ipsum</li></ul>
  <h4 style="left:334px">Our Company</h4>
  <ul class="col" style="left:334px"><li>Lorem ipsum</li><li>Lorem ipsum</li><li>Lorem ipsum</li><li>Lorem ipsum</li></ul>
  <h4 style="left:439px">Support</h4>
  <ul class="col" style="left:437px"><li>Lorem ipsum</li><li>Lorem ipsum</li><li>Lorem ipsum</li><li>Lorem ipsum</li></ul>
  <h4 style="left:534px">Newsletter</h4>
  <p class="col newsletter-text">In venenatis neque a eros laoreet eu placerat erat suscipit. Fusce cursus, erat ut scelerisque condimentum</p>
  <div class="abs newsletter-input">Enter youremail here
    <svg width="5" height="7" viewBox="0 0 5 7"><path d="M0 0l5 3.5L0 7z" fill="#666"/></svg>
  </div>
</footer>
<div class="abs base">Copyright © 2013 Leasewell All rights reserved.</div>

</body>
</html>
```